Town Planning business needs a design (template) for planning reports and letters

I'm looking to develop a report and a letter template. I prepare town planning reports in NSW, Australia. Fairly straight forward reports which would include figures and tables. I can provide examples of similar reports. I have a logo design which I can also provide ( I have attached one file).

Target Market(s)

Professionals, local and state governments

Industry/Entity Type

Property Development

Requirements
Must have
• Title page, contents, 3 - 4 levels of headings, tables and ability to inset figures/photos and Annexure pages at end of report
Nice to have
• Ability to include short details of project in header or footer

```html
<!DOCTYPE html>
<html lang="en">
<head>
<meta charset="utf-8">
<title>Statement of Environmental Effects – Report Template</title>
<link href="https://fonts.googleapis.com/css2?family=Roboto:wght@300;400;500;700&display=swap" rel="stylesheet">
<style>
  :root{
    --backdrop:#9e9e9e;
    --cover-blue:#0a77bc;
    --accent:#1aa3e8;
    --heading-blue:#1a7cc2;
    --paper:#ffffff;
    --body-text:#3a3a3a;
    --muted:#8a8a8a;
  }
  *{box-sizing:border-box;margin:0;padding:0}
  html,body{width:1200px;height:845px;overflow:hidden}
  body{background:var(--backdrop);font-family:'Roboto',sans-serif;position:relative}

  .page{position:absolute;top:36px;width:557px;height:791px;overflow:hidden}
  .cover{left:36px;background:var(--cover-blue)}
  .content{left:615px;background:var(--paper)}

  /* cover */
  .cover-title{position:absolute;left:45px;top:231px;padding-left:14px;border-left:3px solid var(--accent);color:#fff;line-height:30px;font-weight:400}
  .cover-title .lead{font-weight:300;font-size:21px;letter-spacing:.2px}
  .cover-title .main{font-weight:500;font-size:23px;letter-spacing:.3px}

  .credit-band{position:absolute;left:0;top:561px;width:557px;height:115px;background:var(--paper)}
  .credit{position:absolute;top:10px;text-align:center;color:var(--muted);font-weight:300;font-size:14px}
  .credit-by{left:0;width:318px}
  .credit-for{left:318px;width:239px}
  .credit-divider{position:absolute;left:318px;top:20px;width:1px;height:85px;background:#d5d5d5}
  .brand{display:flex;align-items:center;justify-content:center;gap:10px;margin-top:8px}
  .brand-mark{width:36px;height:36px;background:var(--accent);border-radius:50%;flex:none}
  .brand-name{font-weight:700;font-size:21px;color:#222;line-height:22px;text-align:left;text-transform:uppercase;letter-spacing:.3px}
  .client-mark{width:44px;height:44px;background:#e1b12c;border-radius:50%;flex:none}
  .client-name{font-weight:700;font-size:13px;color:#1f3d8f;line-height:16px;text-align:left}
  .job-no{position:absolute;left:34px;top:91px;font-size:11.5px;font-weight:300;color:var(--muted)}

  .contact{position:absolute;left:0;top:696px;width:557px;text-align:center;color:#fff;font-size:12.5px;line-height:17.5px;font-weight:300;font-style:normal}
  .contact b{font-weight:400}

  /* content page */
  .margin-rule{position:absolute;left:56px;top:0;width:1px;height:765px;background:var(--heading-blue)}
  .margin-dot{position:absolute;left:49px;top:42px;width:15px;height:15px;border-radius:50%;background:var(--accent)}
  .chapter{position:absolute;left:75px;top:32px;font-size:27px;font-weight:300;color:var(--heading-blue);letter-spacing:.3px}
  .section-heading{position:absolute;left:75px;font-size:18px;font-weight:300;color:var(--heading-blue)}
  .body{position:absolute;left:79px;width:443px;font-size:12px;letter-spacing:.25px;font-weight:300;color:var(--body-text);line-height:17px;text-align:justify}
  .body p+p{margin-top:17px}
  .purpose-list{list-style:none;margin-top:2px;font-size:12.5px}
  .purpose-list li{position:relative;padding-left:22px;line-height:19px;text-align:left}
  .purpose-list li::before{content:"";position:absolute;left:7px;top:6px;width:7px;height:7px;border-radius:50%;background:var(--accent)}
  .purpose-list li.cont::before{display:none}

  .footer-rule{position:absolute;left:29px;top:728px;width:528px;height:1px;background:var(--accent)}
  .footer-mark{position:absolute;left:480px;top:707px;width:42px;height:42px;border-radius:50%;background:#fff;border:1px solid var(--accent)}
  .page-no{position:absolute;left:31px;top:740px;font-size:18px;font-weight:300;color:var(--heading-blue)}
  .file-path{position:absolute;left:68px;top:746px;font-size:10.5px;font-weight:300;color:#444}
</style>
</head>
<body>

<section class="page cover">
  <h1 class="cover-title">
    <span class="lead">STATEMENT OF</span><br>
    <span class="main">ENVIRONMENTAL EFFECTS TO ACCOMPANY<br>AN AMENDED DEVELOPMENT APPLICATION</span>
  </h1>

  <div class="credit-band">
    <div class="credit credit-by">By:
      <div class="brand"><span class="brand-mark"></span><span class="brand-name">Stoneleaf<br>Planning</span></div>
    </div>
    <div class="credit-divider"></div>
    <div class="credit credit-for">Prepared for
      <div class="brand"><span class="client-mark"></span><span class="client-name">Willow Tree<br>Early Learning</span></div>
    </div>
    <p class="job-no">Job No. 14-002&nbsp; amended SEE draft v1 August 2014</p>
  </div>

  <address class="contact">
    21 ORCHARD LANE GLENMORE NSW • &nbsp;PO BOX 210 GLENMORE NSW 2009<br>
    <b>TELEPHONE</b> : [02] 9000 1234 &nbsp; • <b>FAX</b> [02] 9000 1235<br>
    <b>EMAIL:</b> hello@stoneleafplanning.com.au &nbsp; • <b>WEB SITE:</b> www.stoneleafplanning.com.au
  </address>
</section>

<section class="page content">
  <div class="margin-rule"></div>
  <div class="margin-dot"></div>
  <h2 class="chapter">INTRODUCTION</h2>

  <h3 class="section-heading" style="top:89px">1.1 Overview</h3>
  <div class="body" style="top:119px">
    <p>This Statement of Environmental Effects (“SEE”) has been prepared on behalf of Willow Tree Child Care Centre (“the Centre”) to accompany an amended Development Application (“DA”) lodged pursuant to Section 78A of the Environmental Planning and Assessment Act 1979 for alterations and additions to No.48 Kellner Road, Marlow Park (“the site”) for use as a child care centre.</p>
    <p>Following receipt of Council’s letter dated 3 July 2014 and detailed design analysis by Willow Tree the proposed development has now been modified.</p>
    <p>This SEE has been prepared to demonstrate that the proposed development as amended is acceptable in terms of potential environmental impact.</p>
  </div>

  <h3 class="section-heading" style="top:391px">1.2&nbsp; Purpose of the Statement of Environmental Effects</h3>
  <div class="body" style="top:423px">
    <p style="text-align:left;font-size:12.5px">The purpose of this SEE is to:</p>
    <ul class="purpose-list">
      <li>describe the site to which the DA relates;</li>
      <li>describe the character of the surrounding locality and in particular adjoining and adjacent development;</li>
      <li>define the statutory planning framework within which the amended DA is to be assessed and determined;</li>
      <li>describe the form of the proposed development as amended; and</li>
      <li class="cont">assess the proposed development as amended in the light of all the relevant heads of consideration.</li>
    </ul>
  </div>

  <div class="footer-rule"></div>
  <div class="footer-mark"></div>
  <span class="page-no">01</span>
  <span class="file-path">Studio Drive:Users:Dana:SharedFiles:Work:amended see v3.docx</span>
</section>

</body>
</html>
```